BPH Business Card 2018

Brellmore Chiropractic. We have two locations that we want to advertise on the same card. Calderwick OrthoAxis campus address: 3815 Pemberly Dr., Suite 240, Flowood, MS 39587. Madison address: 426 Larkmoor Dr., Building D., Madison, MS 39674. website: www.drbrellmore.example. o:(601)555-0148 f:(601)555-0173

Target Market(s)

Health care decision makers: primary care doctors and mothers

Contact Information for Business Card

I have no idea; up for any suggestions and I'd do much better picking from examples versus describing what I'm looking for. We are in a very high end location and would like the cards to look really sharp.

Requirements
Must have
• My name, Tobias R Venmark, D.C.

```html
<!DOCTYPE html>
<html lang="en">
<head>
<meta charset="utf-8">
<title>Brellmore Chiropractic Business Card</title>
<link href="https://fonts.googleapis.com/css2?family=Cinzel:wght@400&family=Crimson+Text:ital,wght@0,400;1,600&family=Montserrat:wght@400&display=swap" rel="stylesheet">
<style>
  :root {
    --bg: #e9e9e9;
    --ink-dark: #1c1c1c;
    --ink-mid: #2e2e2e;
    --paper: #f6f6f6;
    --band: #bdbdbd;
    --silver: #e4e4e4;
    --text-dark: #2a2a2a;
    --text-soft: #cfcfcf;
  }
  * { margin: 0; padding: 0; box-sizing: border-box; }
  html, body { width: 1200px; height: 993px; overflow: hidden; background: var(--bg); }
  .canvas { position: relative; width: 1200px; height: 993px; }
  .card {
    position: absolute; left: 200px; width: 800px; height: 457px;
    border-radius: 22px; overflow: hidden;
    box-shadow: 0 6px 18px rgba(0,0,0,.18);
  }
  .card--front { top: 26px; background: linear-gradient(160deg, var(--ink-mid), var(--ink-dark)); }
  .card--back { top: 510px; }
  .card__shapes { position: absolute; inset: 0; }
  .brand {
    position: absolute; font-family: "Cinzel", serif; font-weight: 400;
    line-height: 1;
  }
  .card--front .brand { left: 200px; top: 140px; color: var(--silver); }
  .brand__name { display: block; font-size: 64px; letter-spacing: 1px; }
  .brand__sub { display: block; font-size: 36px; letter-spacing: 3px; margin-top: 6px; }
  .front__web {
    position: absolute; left: 0; right: 0; top: 320px; text-align: center;
    font-family: "Crimson Text", serif; font-size: 22px; letter-spacing: 2px; color: #bdbdbd;
  }
  .card--back .brand { left: 60px; top: 60px; color: var(--text-dark); }
  .card--back .brand__name { font-size: 44px; }
  .card--back .brand__sub { font-size: 25px; letter-spacing: 2px; }
  .locations { position: absolute; left: 60px; top: 185px; font-family: "Crimson Text", serif; color: var(--text-dark); font-size: 24px; line-height: 1.2; }
  .location + .location { margin-top: 12px; }
  .location__name { font-style: italic; font-weight: 600; }
  .person { position: absolute; left: 498px; top: 70px; color: #fff; }
  .person__name { font-family: "Crimson Text", serif; font-size: 28px; line-height: 1.1; }
  .person__title { font-family: "Crimson Text", serif; font-size: 19px; color: var(--text-soft); }
  .contact { list-style: none; margin-top: 26px; font-family: "Montserrat", sans-serif; font-size: 17px; color: #f0f0f0; }
  .contact li { display: flex; align-items: center; gap: 12px; margin-bottom: 10px; }
  .contact svg { width: 18px; height: 18px; flex: none; fill: none; stroke: #f0f0f0; stroke-width: 1.6; }
</style>
</head>
<body>
<div class="canvas">

  <section class="card card--front">
    <div class="brand">
      <span class="brand__name">BRELLMORE</span>
      <span class="brand__sub">CHIROPRACTIC</span>
    </div>
    <p class="front__web">www.drbrellmore.example</p>
  </section>

  <section class="card card--back">
    <svg class="card__shapes" viewBox="0 0 800 457" preserveAspectRatio="none">
      <defs>
        <radialGradient id="softBody" cx="0.5" cy="0.5" r="0.6">
          <stop offset="0" stop-color="#2c2c2c"/>
          <stop offset="1" stop-color="#1c1c1c"/>
        </radialGradient>
      </defs>
      <rect width="800" height="457" fill="var(--ink-dark)"/>
      <rect x="470" y="0" width="330" height="457" fill="url(#softBody)" role="img" aria-label="Faint line figure of a human back as background decoration"/>
      <path d="M0 0 H390 Q535 220 405 457 H0 Z" fill="var(--band)"/>
      <path d="M0 0 H360 Q500 220 380 457 H0 Z" fill="var(--paper)"/>
    </svg>

    <div class="brand">
      <span class="brand__name">BRELLMORE</span>
      <span class="brand__sub">CHIROPRACTIC</span>
    </div>

    <div class="locations">
      <div class="location">
        <div class="location__name">Calderwick OrthoAxis Campus</div>
        <div>3815 Pemberly Dr., Suite 240</div>
        <div>Flowood, MS 39587</div>
      </div>
      <div class="location">
        <div class="location__name">Madison</div>
        <div>426 Larkmoor Dr., Building D.</div>
        <div>Madison, MS 39674</div>
      </div>
    </div>

    <div class="person">
      <div class="person__name">Tobias R Venmark, D.C.</div>
      <div class="person__title">Chiropractor</div>
      <ul class="contact">
        <li><svg viewBox="0 0 24 24"><path d="M5 3h4l2 5-3 2a12 12 0 0 0 6 6l2-3 5 2v4a2 2 0 0 1-2 2A18 18 0 0 1 3 5a2 2 0 0 1 2-2z"/></svg>(601)555-0148</li>
        <li><svg viewBox="0 0 24 24"><rect x="3" y="9" width="18" height="9" rx="1"/><path d="M7 9V4h10v5M7 14h10v6H7z"/></svg>(601)555-0173</li>
        <li><svg viewBox="0 0 24 24"><circle cx="12" cy="12" r="9"/><path d="M3 12h18M12 3c3 3 3 15 0 18M12 3c-3 3-3 15 0 18"/></svg>www.drbrellmore.example</li>
      </ul>
    </div>
  </section>

</div>
</body>
</html>
```